Drumbeat Winters (The Tale of a Young Meridian Rifleman)

We are looking for a poster design for what amounts to a 20 x 30 MOVIE POSTER - The time period of this story is just before and after the Harrowmark Frontier War - So think between 1860 and 1865 - Our story centers around a teen living in New York who runs off to join the Meridian Army (North - Blue) and engages in various battles vs the Bramwold Army (South - Grey) - We would like something that brings in all these elements PLUS Cornelius Whitby. The mini-series is based on the journal/letters of the main character so maybe that can be included on the poster as well.

We want to see which designer can be bold and creative - Questions??? Just ask and we will guide you! At the bottom of the poster we need:

By: Dorian P. Voss and Milo T. Brandquist

Target Market(s)

This project is being developed and presented to Executives at KVZ for a Mini-Series

Industry/Entity Type

Film Production

Other font styles liked:
• Designer Choice

Requirements
Must have
• THE TITLE OF THE STORY "Drumbeat Winters"
• Our story centers on an 18 year old boy who joins the Meridian Army (North) in New York and goes to war against the South (Bramwold Army)
• By: Dorian P. Voss and Milo T. Brandquist
Nice to have
• American Flag 1860
• Subdued Image of President Cornelius Whitby
• Journal or old fashioned handwritten letter

```html
<!DOCTYPE html>
<html lang="en">
<head>
<meta charset="utf-8">
<title>Drumbeat Winters — Poster</title>
<link rel="stylesheet" href="https://fonts.googleapis.com/css2?family=Great+Vibes&family=Libre+Baskerville:wght@700&family=Open+Sans:wght@800&display=swap">
<style>
  :root {
    --paper: #efedea;
    --paper-shade: #e2dfdb;
    --wood-light: #e4e4e2;
    --wood-dark: #b9b9b6;
    --wood-seam: #6f6f6c;
    --flag-red: #d90f12;
    --flag-blue: #1a2a78;
    --portrait-ink: #1f4f6e;
    --journal-brown: #4a2f22;
    --journal-edge: #c86a36;
    --ink-black: #0d0d0d;
    --quote-navy: #1b1f86;
    --byline-shadow: #b3121a;
  }
  * { margin: 0; padding: 0; box-sizing: border-box; }
  html, body { width: 850px; height: 1200px; overflow: hidden; background: var(--paper); }
  .poster {
    position: relative;
    width: 850px;
    height: 1200px;
    overflow: hidden;
    background: radial-gradient(ellipse at 50% 40%, var(--paper) 55%, var(--paper-shade) 100%);
  }
  .poster__hero-art {
    position: absolute;
    left: 24px; top: 28px;
    width: 816px; height: 464px;
    background:
      linear-gradient(90deg, var(--flag-blue) 0 40%, transparent 40%),
      linear-gradient(90deg, transparent 55%, rgba(31,79,110,.55) 70%, rgba(31,79,110,.35) 92%, transparent 100%),
      repeating-linear-gradient(180deg, var(--flag-red) 0 34px, var(--paper) 34px 68px);
    opacity: .92;
  }
  .poster__floor {
    position: absolute;
    left: 0; top: 780px;
    width: 850px; height: 420px;
  }
  .poster__journal-art {
    position: absolute;
    left: 0; top: 790px;
    width: 220px; height: 306px;
    background: linear-gradient(160deg, var(--journal-brown) 0%, #2e1c14 70%, var(--journal-edge) 100%);
    border-radius: 0 10px 18px 0;
  }
  .poster__title {
    position: absolute;
    left: 0; top: 548px;
    width: 850px;
    text-align: center;
    font-family: "Great Vibes", cursive;
    font-size: 124px;
    line-height: 1.2;
    color: var(--ink-black);
    white-space: nowrap;
  }
  .poster__quote {
    position: absolute;
    right: 30px; top: 792px;
    width: 620px;
    text-align: right;
    font-family: "Libre Baskerville", serif;
    font-weight: 700;
    font-size: 20px;
    line-height: 44.5px;
    color: var(--quote-navy);
    text-shadow: 0 0 2px rgba(255,255,255,.9);
  }
  .poster__byline {
    position: absolute;
    left: 0; top: 1128px;
    width: 850px;
    text-align: center;
    font-family: "Open Sans", sans-serif;
    font-weight: 800;
    font-size: 35px;
    letter-spacing: -0.5px;
    color: var(--ink-black);
    text-shadow: 2px 2px 0 var(--byline-shadow);
    white-space: nowrap;
  }
</style>
</head>
<body>
<main class="poster">
  <div class="poster__hero-art" role="img" aria-label="Weathered 1860 American flag painted in red and blue, with a subdued ink portrait of President Cornelius Whitby over the stripes"></div>

  <svg class="poster__floor" width="850" height="420" viewBox="0 0 850 420" aria-hidden="true">
    <defs>
      <linearGradient id="floor-shade" x1="0" y1="0" x2="0" y2="1">
        <stop offset="0" stop-color="var(--wood-light)"/>
        <stop offset="1" stop-color="var(--wood-dark)"/>
      </linearGradient>
    </defs>
    <rect width="850" height="420" fill="url(#floor-shade)"/>
    <line x1="0" y1="0" x2="850" y2="0" stroke="var(--wood-seam)" stroke-width="2"/>
    <g stroke="var(--wood-seam)" stroke-width="2" opacity=".7">
      <line x1="108" y1="0" x2="40" y2="420"/>
      <line x1="262" y1="0" x2="228" y2="420"/>
      <line x1="418" y1="0" x2="420" y2="420"/>
      <line x1="576" y1="0" x2="612" y2="420"/>
      <line x1="730" y1="0" x2="800" y2="420"/>
    </g>
  </svg>

  <div class="poster__journal-art" role="img" aria-label="Worn leather journal tied with cord and a brass winged key"></div>

  <h1 class="poster__title">Drumbeat Winters</h1>

  <p class="poster__quote">
    He who serves in battle does not expect to see his own<br>
    name on the title page of history and is content with<br>
    a proper recognition of the old command in which he<br>
    fought. He who serves in battle does not expect to see<br>
    his own name on the title page of history and is<br>
    content with a proper recognition of the old<br>
    command in which he fought.
  </p>

  <p class="poster__byline">By: Dorian P. Voss and Milo T. Brandquist</p>
</main>
</body>
</html>
```